Pharma Business needs a new careers template

We need a new job posting template to use for all of our open positions. We are in the pharma production business and want to elevate our job postings. The design should incorporate our company colours (namely blue and white).<br/><br/>The completed work should look professional, innovative and slightly quirky.<br/><br/>Feel free to familiarise yourself with some of our current designs on our website (www.torvax.com).<br/><br/>We have a few ideas of how we want the template to look like:<br/><br/>- We would like the design to incorporate various boxes that show different information like "Role Profile", "Benefits" etc.<br/><br/>- We would like to show some of our achievements in a special type of ellipses that remind of tablets or capsules. See a close example of another job posting incorporating similar design (but with circles instead of capsules/tablets) attached.<br/><br/>- We would like some of the main information like job location, contact phone etc to be shown after a corresponding icon. Example screenshot applied.<br/><br/>We have also attached an example job posting to give you an idea of what information our template should hold.

Industry/Entity Type

Pharmaceutical

Colors
33a6d7
ffffff
0393ce
3277b5

Requirements
Must have
• The file should be editable so we can freely fill it for each new position. We should also have it in PSD format.

```html
<!DOCTYPE html>
<html lang="en">
<head>
<meta charset="utf-8">
<title>Torvax – Careers Template</title>
<link href="https://fonts.googleapis.com/css2?family=Arimo:wght@400;700&display=swap" rel="stylesheet">
<style>
  :root{
    --blue:#3277b5;
    --blue-deep:#2e6fae;
    --ink:#111;
    --line:#9a9a9a;
    --shadow:#8c8c8c;
    --paper:#fff;
    --stage:#c4c4c4;
  }
  *{box-sizing:border-box;margin:0;padding:0}
  html,body{width:1200px;height:1200px;overflow:hidden}
  body{background:var(--stage);font-family:"Arimo",Arial,sans-serif;color:var(--ink);position:relative}
  .sheet{position:absolute;left:190px;top:20px;width:820px;height:1160px;background:var(--paper)}

  .brand{position:absolute;left:44px;top:52px;display:flex;align-items:center;gap:8px}
  .brand-dot{width:14px;height:14px;border-radius:50%;background:var(--blue)}
  .brand-name{font-size:38px;font-weight:700;color:var(--blue);letter-spacing:.5px}

  .contacts{position:absolute;top:38px;font-size:16px;line-height:25px}
  .contacts li{list-style:none;display:flex;align-items:flex-start;gap:9px;height:25px;white-space:nowrap}
  .contacts .icon{width:17px;height:17px;margin-top:4px;flex:none}
  .contacts--phone{left:239px}
  .contacts--web{left:420px}
  .contacts--addr{left:600px;line-height:20px}
  .contacts--addr li{height:auto}

  .panel{position:absolute;left:43px;width:543px;background:var(--paper);
    border:1px solid var(--line);border-radius:8px;
    box-shadow:3px 3px 0 var(--blue)}
  .panel-title{position:absolute;left:30px;top:-14px;background:var(--paper);padding:0 14px;
    font-size:19px;font-weight:700;color:var(--blue);line-height:24px;white-space:nowrap}
  .panel-title--caps{letter-spacing:4px;font-size:20px;top:-15px}
  .panel-body{position:absolute;left:39px;right:36px;top:30px;font-size:12px;line-height:15px}
  .panel-body ul{list-style:none}
  .panel-body li::before{content:"• "}

  .capsule{position:absolute;left:597px;width:188px;height:74px;border-radius:37px;
    background:var(--blue-deep);box-shadow:3px 3px 0 var(--shadow);
    display:flex;align-items:center;color:#fff;overflow:hidden}
  .capsule-num{font-size:40px;font-weight:700;width:74px;flex:none;text-align:center;padding-left:4px}
  .capsule-text{font-size:12px;font-weight:700;line-height:15px;white-space:nowrap}
</style>
</head>
<body>
<main class="sheet">
  <div class="brand"><span class="brand-dot"></span><span class="brand-name">torvax</span></div>

  <ul class="contacts contacts--phone">
    <li><svg class="icon" viewBox="0 0 20 20"><circle cx="10" cy="10" r="10" fill="#3277b5"/><path d="M5 9c0-2 2.5-3 5-3s5 1 5 3l-2 .5-.5-1.5h-5L7 9.5z M6.5 14l1.5-4h4l1.5 4z" fill="#fff"/></svg>+359 2 48 61 210</li>
    <li><svg class="icon" viewBox="0 0 20 20"><circle cx="10" cy="10" r="10" fill="#3277b5"/><path d="M5 9c0-2 2.5-3 5-3s5 1 5 3l-2 .5-.5-1.5h-5L7 9.5z M6.5 14l1.5-4h4l1.5 4z" fill="#fff"/></svg>+359 2 48 61 211</li>
    <li><svg class="icon" viewBox="0 0 20 20"><circle cx="10" cy="10" r="10" fill="#3277b5"/><path d="M5 9c0-2 2.5-3 5-3s5 1 5 3l-2 .5-.5-1.5h-5L7 9.5z M6.5 14l1.5-4h4l1.5 4z" fill="#fff"/></svg>+359 2 48 61 212</li>
  </ul>
  <ul class="contacts contacts--web">
    <li><svg class="icon" viewBox="0 0 20 20"><circle cx="10" cy="10" r="10" fill="#3277b5"/><rect x="5" y="6.5" width="10" height="7" rx="1" fill="none" stroke="#fff" stroke-width="1.4"/><path d="M5.5 7l4.5 4 4.5-4" fill="none" stroke="#fff" stroke-width="1.4"/></svg>office@torvax.com</li>
    <li><svg class="icon" viewBox="0 0 20 20"><circle cx="10" cy="10" r="10" fill="#3277b5"/><circle cx="10" cy="10" r="5" fill="none" stroke="#fff" stroke-width="1.3"/><path d="M5 10h10M10 5c-2.5 3-2.5 7 0 10M10 5c2.5 3 2.5 7 0 10" fill="none" stroke="#fff" stroke-width="1"/></svg>torvax.com</li>
  </ul>
  <ul class="contacts contacts--addr">
    <li><svg class="icon" viewBox="0 0 20 20"><circle cx="10" cy="10" r="10" fill="#3277b5"/><path d="M5 10l5-4.5 5 4.5h-1.5v4.5h-7V10z" fill="#fff"/><rect x="9" y="11.5" width="2" height="3" fill="#3277b5"/></svg><span>27 Linden Str.<br>1410 Varnel<br>Bulgaria</span></li>
  </ul>

  <section class="panel" style="top:153px;height:177px">
    <h2 class="panel-title panel-title--caps">JOB TITLE</h2>
    <div class="panel-body">
      <p>Habitasse porta luctus porta. Aptent augue. Justo aliquet urna justo. Inceptos ligula elit aenean maecenas montes ullamcorper commodo volutpat Massa aliquam velit interdum viverra congue malesuada lacus lobortis egestas malesuada blandit nec facilisis. Fermentum tempor arcu litora fringilla, quis aenean sagittis feugiat a pretium hendrerit sociosqu mattis, maecenas.</p>
      <p>Turpis lorem. Aliquet nibh sociis mus facilisi interdum aliquet aenean sem vulputate natoque. Malesuada rutrum sociosqu sociosqu litora nunc ornare feugiat volutpat feugiat natoque dictumst scelerisque sociis ornare Eget inceptos quam interdum.</p>
    </div>
  </section>

  <section class="panel" style="top:368px;height:145px">
    <h2 class="panel-title">Role Profile:</h2>
    <div class="panel-body">
      <p>Velit Commodo, ultrices proin tellus montes magnis mi porttitor metus sociis condimentum dis platea. Ad consectetuer laoreet euismod ad donec tellus elit ad metus lectus. Sit pretium quis imperdiet velit turpis diam urna torquent ante phasellus nascetur per euismod ultrices consectetuer a. Sollicitudin lobortis scelerisque vel senectus id, pharetra iaculis non sem id nam odio fames facilisi quam integer condimentum rutrum pulvinar inceptos. Montes id nonummy platea, mattis proin cum.</p>
    </div>
  </section>

  <section class="panel" style="top:552px;height:180px">
    <h2 class="panel-title">To be successful in this role you should have:</h2>
    <div class="panel-body">
      <ul>
        <li>Cubilia. Porta. Morbi aliquet aptent Aenean nostra purus.</li>
        <li>Rhoncus vitae mus fermentum placerat placerat libero.</li>
        <li>Interdum, dapibus aliquet dignissim hac fusce non. Consectetuer.</li>
        <li>Quam hac, ornare hendrerit ultricies.</li>
        <li>Netus parturient elementum, nisi purus dui.</li>
        <li>Justo sodales, suspendisse fermentum, quisque fermentum quisque pulvinar.</li>
        <li>Convallis lectus feugiat suspendisse ullamcorper nonummy duis pretium.</li>
        <li>Eget pretium per tempor natoque. Quisque.</li>
      </ul>
    </div>
  </section>

  <section class="panel" style="top:773px;height:145px">
    <h2 class="panel-title">Benefits:</h2>
    <div class="panel-body">
      <ul>
        <li>Nonummy fermentum nec dictumst et.</li>
        <li>Venenatis. Aenean ac. Commodo volutpat dolor libero mus.</li>
        <li>Cras consequat, non tempor justo.</li>
        <li>Natoque potenti Hymenaeos ad tristique torquent ultrices. Nec donec. Eu.</li>
        <li>Ac consequat ridiculus convallis curae; porttitor.</li>
        <li>Lobortis non hendrerit taciti sed. Cursus.</li>
      </ul>
    </div>
  </section>

  <section class="panel" style="top:961px;height:152px">
    <h2 class="panel-title">Challenged by this career opportunity?</h2>
    <div class="panel-body">
      <p>Curae; eros cubilia suspendisse netus turpis laoreet nonummy vivamus scelerisque rutrum.</p>
      <p>Risus porttitor semper erat lorem ante orci cum natoque mauris lobortis. Velit semper aliquet. Metus proin ullamcorper augue urna. Eros taciti maecenas est, aliquam parturient etiam gravida nullam molestie. Sem imperdiet.</p>
      <p>Porta praesent sit. Vitae pede luctus et potenti ac augue primis cum vel. Blandit scelerisque tincidunt tincidunt luctus pretium eleifend.</p>
    </div>
  </section>

  <div class="capsule" style="top:162px"><span class="capsule-num">50</span><span class="capsule-text">Nunc quis<br>mauris vitae<br>nunc gravida po-</span></div>
  <div class="capsule" style="top:255px"><span class="capsule-num">50</span><span class="capsule-text">Nunc quis<br>mauris vitae<br>nunc gravida po-</span></div>
  <div class="capsule" style="top:352px"><span class="capsule-num">50</span><span class="capsule-text">Nunc quis<br>mauris vitae<br>nunc gravida po-</span></div>
  <div class="capsule" style="top:445px"><span class="capsule-num">50</span><span class="capsule-text">Nunc quis<br>mauris vitae<br>nunc gravida po-</span></div>
  <div class="capsule" style="top:546px"><span class="capsule-num">50</span><span class="capsule-text">Nunc quis<br>mauris vitae<br>nunc gravida po-</span></div>
  <div class="capsule" style="top:639px"><span class="capsule-num">50</span><span class="capsule-text">Nunc quis<br>mauris vitae<br>nunc gravida po-</span></div>
  <div class="capsule" style="top:736px"><span class="capsule-num">50</span><span class="capsule-text">Nunc quis<br>mauris vitae<br>nunc gravida po-</span></div>
  <div class="capsule" style="top:829px"><span class="capsule-num">50</span><span class="capsule-text">Nunc quis<br>mauris vitae<br>nunc gravida po-</span></div>
  <div class="capsule" style="top:929px"><span class="capsule-num">50</span><span class="capsule-text">Nunc quis<br>mauris vitae<br>nunc gravida po-</span></div>
  <div class="capsule" style="top:1022px"><span class="capsule-num">50</span><span class="capsule-text">Nunc quis<br>mauris vitae<br>nunc gravida po-</span></div>
</main>
</body>
</html>
```